K.D. Roofing LLC
President
K.D. Roofing LLC - Construction
Creative Brief
Professional
Mark Delvane III
4718 Falconer Ridge Lane Cherry Hill, NJ 08517
k.d.roofing.mdelvane@mailbox-example.com
I will be using gloss plastice business cards

```html
<!DOCTYPE html>
<html lang="en">
<head>
<meta charset="utf-8">
<title>K.D. Roofing LLC – Business Cards</title>
<link href="https://fonts.googleapis.com/css2?family=Tinos:ital,wght@0,400;0,700;1,400;1,700&display=swap" rel="stylesheet">
<style>
  :root{
    --bg:#e9ebe8;
    --card:#ffffff;
    --green:#4f9a1c;
    --green-light:#8cc63f;
    --green-dark:#2f6e0c;
    --grey:#b9bcbf;
    --ink:#2b2b2b;
    --name:#3f8a12;
  }
  *{margin:0;padding:0;box-sizing:border-box}
  html,body{width:1200px;height:852px;overflow:hidden;background:var(--bg)}
  .canvas{position:relative;width:1200px;height:852px;font-family:"Tinos","Times New Roman",serif;color:var(--ink)}
  .card{position:absolute;width:620px;height:354px;background:var(--card);border-radius:22px;overflow:hidden;box-shadow:0 2px 6px rgba(0,0,0,.15)}
  .card--a{left:80px;top:70px}
  .card--b{left:500px;top:428px}
  .card .swoosh{position:absolute;inset:0;width:100%;height:100%}
  .brand{position:absolute;display:flex;align-items:center;gap:12px}
  .brand__dot{width:46px;height:46px;border-radius:50%;background:var(--green)}
  .brand__name{font-family:"Tinos","Times New Roman",serif;font-weight:700;font-size:27px;color:var(--green);letter-spacing:.5px;white-space:nowrap}
  .person__name{font-style:italic;font-weight:700;font-size:20px;color:var(--name)}
  .person__role{font-style:italic;font-size:13px;color:var(--green)}
  .address{font-size:15px;line-height:20px}
  .divider{position:absolute;width:1px;background:var(--grey)}
  .contacts{position:absolute;list-style:none;font-size:12px;line-height:26px}
  .contacts li{display:flex;align-items:center;gap:8px;white-space:nowrap}
  .contacts svg{width:13px;height:13px;flex:none;fill:var(--ink)}

  .card--a .brand{left:60px;top:80px}
  .card--a .person{position:absolute;right:340px;top:172px;text-align:right}
  .card--a .address{position:absolute;left:58px;top:228px}
  .card--a .divider{left:296px;top:170px;height:118px}
  .card--a .contacts{left:310px;top:168px}

  .card--b .person{position:absolute;left:300px;top:70px}
  .card--b .brand{left:20px;top:120px;width:248px;flex-direction:column;gap:10px}
  .card--b .brand__dot{width:58px;height:58px}
  .card--b .brand__name{font-size:23px}
  .card--b .divider{left:284px;top:70px;height:240px}
  .card--b .address{position:absolute;left:300px;top:140px}
  .card--b .contacts{left:300px;top:208px}
</style>
</head>
<body>
<main class="canvas">

  <section class="card card--a" aria-label="Business card, layout one">
    <svg class="swoosh" viewBox="0 0 620 354" aria-hidden="true">
      <defs>
        <linearGradient id="greenBandA" x1="0" y1="0" x2="1" y2="1">
          <stop offset="0" stop-color="#8cc63f"/><stop offset="1" stop-color="#2f6e0c"/>
        </linearGradient>
      </defs>
      <path d="M440 0 C520 10 590 50 620 110 L620 0 Z" fill="url(#greenBandA)"/>
      <path d="M410 0 C510 14 590 60 620 130" fill="none" stroke="#b9bcbf" stroke-width="5"/>
      <path d="M0 240 C40 300 120 340 230 354 L0 354 Z" fill="url(#greenBandA)"/>
      <path d="M0 222 C40 290 130 336 250 354" fill="none" stroke="#b9bcbf" stroke-width="5"/>
    </svg>
    <div class="brand"><span class="brand__dot"></span><span class="brand__name">K.D. Roofing LLC</span></div>
    <div class="person">
      <p class="person__name">Mark Delvane III</p>
      <p class="person__role">President</p>
    </div>
    <p class="address">4718 Falconer Ridge Lane<br>Cherry Hill, NJ 08517</p>
    <span class="divider"></span>
    <ul class="contacts">
      <li><svg viewBox="0 0 24 24"><path d="M6.6 10.8a15 15 0 0 0 6.6 6.6l2.2-2.2a1 1 0 0 1 1-.25 11.4 11.4 0 0 0 3.6.57 1 1 0 0 1 1 1V20a1 1 0 0 1-1 1A17 17 0 0 1 3 4a1 1 0 0 1 1-1h3.5a1 1 0 0 1 1 1c0 1.25.2 2.450.57 3.57a1 1 0 0 1-.25 1z"/></svg>856-555-0142</li>
      <li><svg viewBox="0 0 24 24"><path d="M7 1h10a2 2 0 0 1 2 2v18a2 2 0 0 1-2 2H7a2 2 0 0 1-2-2V3a2 2 0 0 1 2-2zm0 3v14h10V4zm5 15.5a1 1 0 1 0 0 2 1 1 0 0 0 0-2z"/></svg>856-555-0187</li>
      <li><svg viewBox="0 0 24 24"><path d="M12 2a10 10 0 1 0 5 18.7l-1-1.7A8 8 0 1 1 20 12v1a2 2 0 0 1-4 0V7h-2v1a5 5 0 1 0 .6 7A4 4 0 0 0 22 13v-1A10 10 0 0 0 12 2zm0 13a3 3 0 1 1 0-6 3 3 0 0 1 0 6z"/></svg>k.d.roofing.mdelvane@mailbox-example.com</li>
    </ul>
  </section>

  <section class="card card--b" aria-label="Business card, layout two">
    <svg class="swoosh" viewBox="0 0 620 354" aria-hidden="true">
      <defs>
        <linearGradient id="greenBandB" x1="0" y1="0" x2="1" y2="1">
          <stop offset="0" stop-color="#8cc63f"/><stop offset="1" stop-color="#2f6e0c"/>
        </linearGradient>
      </defs>
      <path d="M440 0 C520 10 590 50 620 110 L620 0 Z" fill="url(#greenBandB)"/>
      <path d="M410 0 C510 14 590 60 620 130" fill="none" stroke="#b9bcbf" stroke-width="5"/>
      <path d="M0 280 C60 320 140 344 260 354 L0 354 Z" fill="url(#greenBandB)"/>
      <path d="M0 262 C60 312 150 340 280 354" fill="none" stroke="#b9bcbf" stroke-width="5"/>
    </svg>
    <div class="person">
      <p class="person__name">Mark Delvane III</p>
      <p class="person__role">President</p>
    </div>
    <div class="brand"><span class="brand__dot"></span><span class="brand__name">K.D. Roofing LLC</span></div>
    <span class="divider"></span>
    <p class="address">4718 Falconer Ridge Lane<br>Cherry Hill, NJ 08517</p>
    <ul class="contacts">
      <li><svg viewBox="0 0 24 24"><path d="M6.6 10.8a15 15 0 0 0 6.6 6.6l2.2-2.2a1 1 0 0 1 1-.25 11.4 11.4 0 0 0 3.6.57 1 1 0 0 1 1 1V20a1 1 0 0 1-1 1A17 17 0 0 1 3 4a1 1 0 0 1 1-1h3.5a1 1 0 0 1 1 1c0 1.25.2 2.45.57 3.57a1 1 0 0 1-.25 1z"/></svg>856-555-0142</li>
      <li><svg viewBox="0 0 24 24"><path d="M7 1h10a2 2 0 0 1 2 2v18a2 2 0 0 1-2 2H7a2 2 0 0 1-2-2V3a2 2 0 0 1 2-2zm0 3v14h10V4zm5 15.5a1 1 0 1 0 0 2 1 1 0 0 0 0-2z"/></svg>856-555-0187</li>
      <li><svg viewBox="0 0 24 24"><path d="M12 2a10 10 0 1 0 5 18.7l-1-1.7A8 8 0 1 1 20 12v1a2 2 0 0 1-4 0V7h-2v1a5 5 0 1 0 .6 7A4 4 0 0 0 22 13v-1A10 10 0 0 0 12 2zm0 13a3 3 0 1 1 0-6 3 3 0 0 1 0 6z"/></svg>k.d.roofing.mdelvane@mailbox-example.com</li>
    </ul>
  </section>

</main>
</body>
</html>
```